Social Media Overlay for Ormond Real Estate

We need an social media overlay that can be added to a photo of a house that includes our current logo and a call to action of "Just Listed". This needs to be something that we can use for every new house that we list. Attached is our current logo in both company colors, purple and white. An example of a overlay from Plazeo that we like.

Target Market(s)

Social Media Real Estate Community - Real Estate Agents, Brokers, Buyers & Sellers

Industry/Entity Type

Real Estate

Font styles to use
Sans Serif

Colors
6c459b

Requirements
Must have
• the company colors, purple and white and the company logo
Nice to have
• call to action "Just Listed"
• some layered, texture, or 3-D effect
Should not have
• Should be clean and simple; nothing too busy

```html
<!DOCTYPE html>
<html lang="en">
<head>
<meta charset="utf-8">
<title>Ormond Real Estate – Just Listed Overlay</title>
<link rel="stylesheet" href="https://fonts.googleapis.com/css2?family=Montserrat:wght@500;800&display=swap">
<style>
  :root {
    --brand-purple: #6c459b;
    --badge-deep: #2a0f3d;
    --badge-mid: #5b2a80;
    --badge-ring: #7a3fb0;
    --white: #ffffff;
    --stage-light: #bdbdbd;
    --stage-dark: #8a8a8a;
    --stage-border: #ffffff;
  }
  * { box-sizing: border-box; margin: 0; padding: 0; }
  html, body { width: 1200px; height: 1200px; overflow: hidden; background: var(--stage-border); }
  .stage {
    position: absolute; left: 20px; top: 20px; width: 1160px; height: 1160px;
    background: linear-gradient(180deg, var(--stage-dark) 0%, var(--stage-light) 50%, var(--stage-dark) 100%);
  }
  .post {
    position: absolute; left: 134px; width: 928px; height: 486px; overflow: hidden;
    box-shadow: 2px 3px 6px rgba(0,0,0,0.35);
  }
  .post--top { top: 35px; }
  .post--bottom { top: 590px; }
  .photo { position: absolute; inset: 0; }
  .photo--dusk {
    background: linear-gradient(180deg, #1f6fd8 0%, #3e8ae6 22%, #6b5a48 42%, #8a6a4c 58%, #6a4a40 70%, #3f6a2c 82%, #2f5a22 100%);
  }
  .photo--craftsman {
    background: linear-gradient(180deg, #b8cde0 0%, #3f5a3c 18%, #4a4f6e 45%, #4a4f6e 62%, #8a8a86 74%, #4e9a36 84%, #3f8a2a 100%);
  }
  .listing-band {
    position: absolute; left: 734px; top: 381px; width: 194px; height: 73px;
    background: linear-gradient(90deg, rgba(255,255,255,0.25) 0%, rgba(255,255,255,0.55) 40%, rgba(255,255,255,0.5) 100%);
    display: flex; flex-direction: column; justify-content: center; align-items: center;
    padding-left: 18px;
    font-family: "Montserrat", sans-serif; font-weight: 800; color: var(--brand-purple);
    line-height: 1.05;
  }
  .listing-band .brand-name { font-size: 27px; letter-spacing: -0.5px; }
  .listing-band .brand-sub { font-size: 15px; }
  .badge {
    position: absolute; left: 640px; top: 357px; width: 110px; height: 110px; border-radius: 50%;
    background: radial-gradient(circle at 50% 45%, var(--badge-mid) 0%, #3d1658 45%, var(--badge-deep) 100%);
    border: 3px solid var(--badge-ring);
    box-shadow: 0 2px 6px rgba(0,0,0,0.5);
    display: flex; flex-direction: column; justify-content: center; align-items: center;
    font-family: "Montserrat", sans-serif; font-weight: 800; color: var(--white);
    font-size: 18px; line-height: 1.55; text-align: center;
  }
</style>
</head>
<body>
  <div class="stage">
    <section class="post post--top">
      <div class="photo photo--dusk" role="img" aria-label="Photo of a Mediterranean-style house at dusk with palm trees, lit facade and brick-paved driveway"></div>
      <div class="listing-band"><span class="brand-name">Ormond</span><span class="brand-sub">Real Estate</span></div>
      <div class="badge"><span>JUST</span><span>LISTED!</span></div>
    </section>
    <section class="post post--bottom">
      <div class="photo photo--craftsman" role="img" aria-label="Photo of a navy craftsman-style house with white trim, stone column bases, pine trees and a green lawn"></div>
      <div class="listing-band"><span class="brand-name">Ormond</span><span class="brand-sub">Real Estate</span></div>
      <div class="badge"><span>JUST</span><span>LISTED!</span></div>
    </section>
  </div>
</body>
</html>
```